Car rental website design for a UAE car rental company

This project is about creating a new website design for a car rental company located in Dubai (United Arab Emirates), I opened the same project a few months ago but I didn't receive a lot of appealing entries so I closed it but this time I am marking the project as guaranteed to avoid such situation again, if you have already provided a design before then please re-submit again on this project so that it is considered while reviewing all the designs

A few important things:

1- We need a simple non-complex design
2- The final deliverable would be 2 screens (PSD, JPEG ... etc), the first screen is for the home page and the second screen is for an internal page
3- The home page must have a section that end users can use to rent a car online directly from the home page instead of going into some inner pages
4- The current website is very old and not very appealing so avoid creating a similar design (www.quarvin-drive.example)
5- The name is Quarvin but the company rents normal cars (no Limousin cars will be rented) so avoid adding any fancy cars in the images/graphics used in the design, just normal end users cars
6- The expected pages would be: home, About us, Our team, Strategy, Contact us and links to social media pages
7- The attachments include the company's logo and some screens from other car rental companies that provide online rentals/payments

If you have any questions please feel free to ask and please note that we will need the designs urgently

Thanks

Target Market(s)

Dubai - United Arab Emirates

Industry/Entity Type

It Company

Number of Pages Required

2 page

Font styles to use
Sans Serif

Requirements
Must have
• Check the project details
Nice to have
Should not have

```html
<!DOCTYPE html>
<html lang="en">
<head>
<meta charset="utf-8">
<title>Quarvin – Car Rental</title>
<link href="https://fonts.googleapis.com/css2?family=Roboto:wght@300;400;500;700&family=Lato:wght@400;900&display=swap" rel="stylesheet">
<style>
:root{
  --brand:#a2092e;
  --brand-dark:#8d0627;
  --nav-active:#8e9c97;
  --ink:#1f1f1f;
  --text:#333;
  --muted:#c8c8c8;
  --band:#e5e6e6;
  --white:#fff;
  --field-border:#d9d9d9;
}
*{box-sizing:border-box;margin:0;padding:0}
html,body{width:1061px;height:1200px;overflow:hidden;background:var(--white)}
body{position:relative;font-family:"Roboto",Arial,sans-serif;color:var(--text)}
.abs{position:absolute}

/* header */
.brand{left:124px;top:16px;display:flex;align-items:center;gap:8px}
.brand-mark{width:14px;height:14px;background:var(--brand)}
.brand-name{font-size:22px;font-weight:500;color:var(--brand);letter-spacing:.5px}
.phone{left:756px;top:5px;display:flex;align-items:center;gap:10px;font-size:21px;font-weight:500;color:var(--ink)}
.account{left:788px;top:44px;display:flex;gap:14px;font-size:16px;color:var(--ink)}
.account span{display:flex;align-items:center;gap:5px}

/* nav */
.nav{left:0;top:86px;width:1061px;height:39px;background:var(--brand)}
.nav a{position:absolute;top:0;height:39px;line-height:39px;color:var(--white);text-decoration:none;font-size:16px;font-weight:500}
.nav a.active{background:var(--nav-active);padding:0 15px}

/* hero */
.hero{left:0;top:125px;width:1061px;height:247px;overflow:hidden;background:linear-gradient(90deg,#e9eaea,#f3f3f3 40%,#dcdcdc)}
.hero-photo{position:absolute;left:606px;top:0;width:455px;height:247px}
.hero-arrow{position:absolute;top:109px;width:32px;height:28px;background:rgba(120,120,120,.55);display:flex;align-items:center;justify-content:center}
.search{left:149px;top:172px;width:363px;height:159px;background:rgba(255,255,255,.93)}
.search h2{position:absolute;left:12px;top:6px;font-size:19px;font-weight:300;color:#555}
.search label{position:absolute;font-size:8px;color:#444}
.field{position:absolute;height:22px;border:1px solid var(--field-border);background:var(--white);font-size:6.5px;color:#999;display:flex;align-items:center;gap:5px;padding-left:6px}
.search-btn{position:absolute;left:12px;top:128px;width:80px;height:22px;background:var(--brand);color:var(--white);font-size:8.5px;display:flex;align-items:center;justify-content:center}

/* sections */
.section-title{width:1061px;left:0;text-align:center;color:var(--brand);font-size:24px;font-weight:500}
.lead{width:1061px;left:0;text-align:center;color:var(--ink);font-size:19px}
.intro{left:170px;width:721px;text-align:center;font-size:15.5px;line-height:20px;color:var(--text)}
.feature{width:420px}
.feature h3{display:flex;align-items:center;gap:10px;font-size:14.5px;font-weight:500;color:var(--ink)}
.feature p{margin-top:10px;font-size:11px;line-height:15px;color:var(--text)}

.services{left:0;top:736px;width:1061px;height:322px;background:var(--band)}
.svc{font-size:13.5px;color:var(--ink);display:flex;align-items:center}
.svc::before{content:"»";position:absolute;left:-26px;color:var(--brand);font-weight:700;font-size:17px;top:-4px}
.sub{font-size:13.5px;color:var(--brand);line-height:19.5px}
.divider{left:518px;top:847px;width:1px;height:189px;background:var(--brand)}

/* signup */
.signup-title{left:125px;top:1091px;font-family:"Lato",Arial,sans-serif;font-weight:900;font-size:21px;color:var(--ink)}
.signup-sub{left:125px;top:1119px;font-family:"Lato",Arial,sans-serif;font-size:11.5px;color:var(--muted)}
.email{left:467px;top:1090px;width:297px;height:43px;border:2px solid var(--brand)}
.email span{position:absolute;left:23px;top:12px;font-size:10px;color:#888}
.send{position:absolute;right:17px;top:7px;width:48px;height:24px;border:1px solid #999;font-size:11px;color:#555;display:flex;align-items:center;justify-content:center}
.social{top:1092px;width:46px;height:38px}
.footer{left:0;top:1163px;width:1061px;height:37px;background:var(--brand);color:var(--white);font-size:11.5px;text-align:center;line-height:37px}
</style>
</head>
<body>

<header>
  <div class="abs brand"><span class="brand-mark"></span><span class="brand-name">Quarvin</span></div>
  <div class="abs phone">
    <svg width="28" height="28" viewBox="0 0 28 28"><circle cx="14" cy="14" r="12.5" fill="none" stroke="var(--brand)" stroke-width="1.6"/><path d="M10 8c1 0 2 2.5 2 3s-1 1-1 1.5 2.5 4 4 4.5c.5 0 1-1 1.5-1s3 1 3 2-1.5 2.5-2.5 2.5C12 20 8 15 8 10c0-1 1-2 2-2z" fill="var(--brand)"/></svg>
    (555) 014-2290
  </div>
  <div class="abs account">
    <span><svg width="12" height="14" viewBox="0 0 12 14"><rect x="1" y="6" width="10" height="8" fill="#888"/><path d="M3 6V4a3 3 0 016 0v2" fill="none" stroke="#888" stroke-width="1.6"/></svg>Login</span>
    <span><svg width="15" height="15" viewBox="0 0 15 15"><circle cx="7.5" cy="7.5" r="6.5" fill="none" stroke="#888" stroke-width="1.3"/><circle cx="7.5" cy="6" r="2.3" fill="#888"/><path d="M3.5 12c1-2 2.3-3 4-3s3 1 4 3" fill="#888"/></svg>SignUp</span>
  </div>
</header>

<nav class="abs nav">
  <a style="left:148px">Home</a>
  <a class="active" style="left:226px">About Us</a>
  <a style="left:359px">Our Team</a>
  <a style="left:468px">Strategy</a>
  <a style="left:564px">Contact Us</a>
</nav>

<section class="abs hero">
  <svg class="hero-photo" viewBox="0 0 455 247" role="img" aria-label="Red coupe parked in a grey concrete showroom">
    <defs><linearGradient id="showroom" x1="0" y1="0" x2="0" y2="1"><stop offset="0" stop-color="#7d8487"/><stop offset=".65" stop-color="#5d6366"/><stop offset="1" stop-color="#1d1f21"/></linearGradient>
    <radialGradient id="carGlow" cx=".55" cy=".6" r=".35"><stop offset="0" stop-color="#c0182c"/><stop offset="1" stop-color="#c0182c" stop-opacity="0"/></radialGradient></defs>
    <polygon points="0,123 50,0 455,0 455,247 50,247" fill="url(#showroom)"/>
    <polygon points="0,123 50,0 455,0 455,247 50,247" fill="url(#carGlow)"/>
  </svg>
  <div class="hero-arrow" style="left:0"><svg width="10" height="14"><path d="M8 1L2 7l6 6" stroke="#fff" stroke-width="2" fill="none"/></svg></div>
  <div class="hero-arrow" style="left:1030px"><svg width="10" height="14"><path d="M2 1l6 6-6 6" stroke="#fff" stroke-width="2" fill="none"/></svg></div>
</section>

<form class="abs search">
  <h2>Search for Rental Cars</h2>
  <label style="left:12px;top:36px">Pick-up From</label>
  <div class="field" style="left:12px;top:46px;width:164px">⌖ City, Airport or U.S. Zip Code</div>
  <label style="left:191px;top:36px">Drop-off To</label>
  <div class="field" style="left:191px;top:46px;width:164px">⌖ City, Airport or U.S. Zip Code</div>
  <label style="left:12px;top:80px">Pick-up Date</label>
  <div class="field" style="left:12px;top:92px;width:74px">▦ mm/dd/yyyy</div>
  <label style="left:101px;top:80px">Pick-up Time</label>
  <div class="field" style="left:101px;top:92px;width:74px">◷ 3:00 PM</div>
  <label style="left:191px;top:80px">Drop-off Date</label>
  <div class="field" style="left:191px;top:92px;width:74px">▦ mm/dd/yyyy</div>
  <label style="left:280px;top:80px">Drop-off Time</label>
  <div class="field" style="left:280px;top:92px;width:74px">◷ 3:00 PM</div>
  <div class="search-btn">Search for Cars</div>
</form>

<section class="about">
  <h1 class="abs section-title" style="top:406px">ABOUT US</h1>
  <p class="abs lead" style="top:446px">We are leading car rental agency with 300,000 Happy Customers.</p>
  <p class="abs intro" style="top:479px">Morbi orci ante,consectetur id vestibulum quis,suscipit eu eros.Duis non egestas dolor.Duis non volutpat leo.Aliquam nisi eros,accumsan non gravida vitae,ultrices eu eros.Phasellsagittis mattis tristique.</p>

  <div class="abs feature" style="left:124px;top:553px">
    <h3><svg width="14" height="14" viewBox="0 0 14 14"><path d="M1 1h6l6 6-6 6-6-6z" fill="var(--brand)"/><circle cx="4" cy="4" r="1.2" fill="#fff"/></svg>Special low rates on car booking</h3>
    <p>Nunc ut nibh enim,id dapibus quam.Mauris id est at diam rutrum etd ultricies.Vivamus et dolor velit.Nam congue blandit nulla sed tincidunt.</p>
  </div>
  <div class="abs feature" style="left:563px;top:553px">
    <h3><svg width="14" height="14" viewBox="0 0 14 14"><rect x="1" y="2" width="11" height="11" fill="none" stroke="var(--brand)" stroke-width="1.8"/><path d="M5 9l7-7" stroke="var(--brand)" stroke-width="2"/></svg>Manage your booking online</h3>
    <p>Aliquam erat volutpat.Pellentesque habitant morbi tristique senectus et netus et malesuada fames ac turpis egestas.</p>
  </div>
  <div class="abs feature" style="left:124px;top:643px">
    <h3><svg width="14" height="14" viewBox="0 0 14 14"><circle cx="7" cy="7" r="5.5" fill="none" stroke="var(--brand)" stroke-width="2.4"/><circle cx="7" cy="7" r="2" fill="none" stroke="var(--brand)" stroke-width="1.2"/></svg>Dedicated customer support</h3>
    <p>Praesent tempus egestas blandit.Nunc euismo volutpat ultrices.Nam fermentum nibh eget mi vehicula dictum.</p>
  </div>
  <div class="abs feature" style="left:563px;top:643px">
    <h3><svg width="14" height="14" viewBox="0 0 14 14"><circle cx="7" cy="7" r="5.8" fill="none" stroke="var(--brand)" stroke-width="1.4"/><circle cx="5" cy="6" r=".9" fill="var(--brand)"/><circle cx="9" cy="6" r=".9" fill="var(--brand)"/><path d="M4.5 9.5c1.5 1.3 3.5 1.3 5 0" stroke="var(--brand)" fill="none"/></svg>You are guaranteed a car</h3>
    <p>Donec vitae orci metus,et viverra ipsum.Curabittristique tristique lacinia. Sed sagittis placerat vestibulum.</p>
  </div>
</section>

<section class="abs services"></section>
<h2 class="abs section-title" style="top:752px">SERVICES</h2>
<p class="abs intro" style="top:790px;color:var(--ink)">Quarvin offers a comprehensive range of services including daily, short term and long term rental, chauffeur drive services for every purpose and budget.</p>

<ul style="list-style:none">
  <li class="abs svc" style="left:150px;top:857px">Wide range of vehicles for city driving or SUV's for trips</li>
  <li class="abs svc" style="left:150px;top:885px;font-weight:500">Special 10% discount for new customers on the first rent</li>
  <li class="abs svc" style="left:150px;top:912px">Long term car rental</li>
  <li class="abs sub" style="left:173px;top:937px">New vehicles<br>Fixed monthly expenditure<br>Free registration and insurance<br>Free maintenance and replacement vehicles<br>No finance costs and no hidden costs</li>
</ul>
<div class="abs divider"></div>
<ul style="list-style:none">
  <li class="abs svc" style="left:590px;top:857px">Buyback option after lease term</li>
  <li class="abs svc" style="left:590px;top:885px">Special offers for online bookings</li>
  <li class="abs svc" style="left:590px;top:912px">Chauffer drive service</li>
  <li class="abs sub" style="left:618px;top:937px;width:320px;line-height:17px">Well-trained and uniformed chauffeurs will ensure passenger satisfaction.</li>
  <li class="abs svc" style="left:590px;top:983px">Airport transfers</li>
  <li class="abs svc" style="left:590px;top:1011px">Sightseeing tours</li>
</ul>

<section class="signup">
  <h2 class="abs signup-title">SIGN UP FOR AMAZING OFFERS</h2>
  <p class="abs signup-sub">EXCLUSIVE ACCESS FOR OFFERS AND PROMOTIONS</p>
  <div class="abs email"><span>Enter your Email Address</span><div class="send">SEND</div></div>
  <div class="abs social" style="left:779px;background:#2d9fd9" role="img" aria-label="Social link"></div>
  <div class="abs social" style="left:832px;background:#d1222d" role="img" aria-label="Social link"></div>
  <div class="abs social" style="left:884px;background:#3b5a9a" role="img" aria-label="Social link"></div>
</section>

<footer class="abs footer">©Copyright 2015, Quarvin. All rights reserved.</footer>

</body>
</html>
```